Executive Powerpoint

A profession presentation with information consumed at a glance. The data is not relevant, just the design. I have an example attached. The components should be the same but the design improved.

Target Market(s)

The company is Brightfold Partners, LLC. We do these presentations for school districts after we build an in-depth report. This is what they use to present the findings to their board.

Industry/Entity Type

Education-School Districts administration level

```html
<!DOCTYPE html>
<html lang="en">
<head>
<meta charset="utf-8">
<title>Survey Findings</title>
<link href="https://fonts.googleapis.com/css2?family=Montserrat:wght@500;600;700;800&display=swap" rel="stylesheet">
<style>
  :root {
    --ink: #111111;
    --navy: #3d4266;
    --coral: #f06a60;
    --accent-blue: #1f6fb8;
    --card-border: #cfeae6;
    --paper: #ffffff;
  }
  * { box-sizing: border-box; margin: 0; padding: 0; }
  html, body { width: 1200px; height: 597px; overflow: hidden; background: var(--paper); }
  .slide {
    position: relative;
    width: 1200px;
    height: 597px;
    background: var(--paper);
    font-family: "Montserrat", sans-serif;
    overflow: hidden;
  }
  .backdrop { position: absolute; inset: 0; }
  .slide-title {
    position: absolute;
    left: 0; right: 0;
    top: 44px;
    text-align: center;
    font-size: 52px;
    font-weight: 800;
    letter-spacing: 1px;
    color: var(--ink);
  }
  .title-rule {
    position: absolute;
    left: 553px;
    top: 114px;
    width: 94px;
    height: 4px;
    background: var(--accent-blue);
  }
  .stat-card {
    position: absolute;
    width: 344px;
    height: 210px;
    background: var(--paper);
    border: 2px solid var(--card-border);
    border-radius: 0 34px 0 34px;
    text-align: center;
    padding: 26px 28px 0;
  }
  .stat-card::after {
    content: "";
    position: absolute;
    left: 50%;
    bottom: -2px;
    width: 116px;
    height: 5px;
    margin-left: -58px;
    background: var(--coral);
  }
  .stat-value {
    font-size: 32px;
    font-weight: 700;
    color: var(--navy);
    margin-bottom: 18px;
  }
  .stat-label {
    font-size: 13.5px;
    font-weight: 600;
    line-height: 1.75;
    color: var(--ink);
  }
  .row-top .stat-card { top: 138px; }
  .row-bottom .stat-card { top: 372px; height: 190px; }
</style>
</head>
<body>
  <main class="slide">
    <svg class="backdrop" width="1200" height="597" viewBox="0 0 1200 597" aria-hidden="true">
      <path d="M1200 0 L1080 0 Q1040 10 1020 80 L800 597 L1200 597 Z" fill="var(--coral)"/>
    </svg>

    <h1 class="slide-title">SURVEY</h1>
    <div class="title-rule"></div>

    <section class="row-top">
      <article class="stat-card" style="left:55px">
        <p class="stat-value">73.5%</p>
        <p class="stat-label">of parents report feeling welcomed and valued at their child's school.</p>
      </article>
      <article class="stat-card" style="left:430px">
        <p class="stat-value">60.2%</p>
        <p class="stat-label">Believe that the programs of this district meet the requirement of students with special needs (handicapped, learning disabled, gifted and talented, etc.).</p>
      </article>
      <article class="stat-card" style="left:806px">
        <p class="stat-value">80.1%</p>
        <p class="stat-label">Agree the district promotes parent-teacher communication.</p>
      </article>
    </section>

    <section class="row-bottom">
      <article class="stat-card" style="left:243px">
        <p class="stat-value">72.4%</p>
        <p class="stat-label">of staff feel supported by district leadership and schools.</p>
      </article>
      <article class="stat-card" style="left:618px">
        <p class="stat-value">70.1%</p>
        <p class="stat-label">express overall satisfaction with their school.</p>
      </article>
    </section>
  </main>
</body>
</html>
```